The Lumo Fenn Organic & Natural Soaps needs a good business card

I am sorry for the lack of direction or Scope of the project. I am new at this board.
This is my scope and requirements:
Business card project:
This is related to the Label project I also opened up. (The Lumo Fenn Organic & Natural Soaps is looking for label designs (along with the business card project (Contest) )
I have attached an initial draft at a logo I tried to come up with for a business card and labelling/marketing. I am hoping that you can take this logo and 'run with it' to finesse it, make it look unique and professional. I am open to new logo ideas.
I am a start up at home company making Organic and Natural Bar soaps, hand soaps, body washes.
All of my ingredients are organic or natural and will include natural essential oils, exfoliants, natural powders/colours, etc.
Some of the names are: Brindlequik (feisty, energetic soap), Vesta (more of a sandalwood earthy tones with a sandalwood powder exfoliant), Tundle (maybe changing this name - fresh scented), Plum Nettle (lemongrass/ginger, exfoliants), etc....
I am attaching the cardstock I am looking at for packaging as well - this might help with the business card aspect. I was originally just looking at plain kraft paper but am receiving samples of Wes Darnby coloured kraft paper. I may still print business cards on the plain kraft though.. not sure.
If you need more information, please let me know.
Mirela
I
Business Card and Labels
I have come up with a basic logo that I like. If you can finesse it and provide a great business card, that would be great.
I am starting up an at home soap business that will include luxury organic bar soaps, luxury natural olive oil bar soaps, organic hand wash, natural olive oil based body wash. I will be selling online and at shows.
please find attached my logo idea that I would like to incorporate.
I am also looking at packaging/labelling ideas for the bar soaps (prefer kraft cardstock wrap) and labels for the various body washes (natural soap) and the hand washes (organic). The hand washes will be in 250ml square bottles and the body wash will be in tapered bottles (smaller at top going to bottom).
Please let me know if you need more info!
I am also looking for packaging (label design for hand soap/body wash bottles and label design for organic/natural soaps)
This Project coincides with the business card project I also posted: there are 2 projects related - 1) business cards, 2) labels for organic hand wash, natural body wash, sticker label or design for kraft paper to package around luxury organic and natural soaps. I am not sure if a sticker would look nice or the design for the thick kraft paper.
Thank you!
Business card project:
This is related to the Label project I also opened up. (The Lumo Fenn Organic & Natural Soaps is looking for label designs (along with the business card proje (Contest) )
I have attached an initial draft at a logo I tried to come up with for a business card and labelling/marketing. I am hoping that you can take this logo and 'run with it' to finesse it, make it look unique and professional.
Mirela
I
Hello; I just wanted to let everyone know that if you feel that this
brand needs a different logo, I am open to ideas (if you don't think the
one I started with is ok). I am coming to the experts here!
Just to confirm also - this is related to the label/packaging project, therefore, there are 2 projects, 2 payments! :)
Cheers

```html
<!DOCTYPE html>
<html lang="en">
<head>
<meta charset="utf-8">
<title>The Lumo Fenn – Business Card</title>
<link rel="stylesheet" href="https://fonts.googleapis.com/css2?family=Lobster+Two:ital,wght@1,700&family=Old+Standard+TT:wght@700&family=Questrial&display=swap">
<style>
  :root {
    --backdrop: #ebe7e1;
    --kraft: #c8a77d;
    --kraft-light: #d1b28a;
    --kraft-dark: #bb9970;
    --orchid: #e1a1d8;
    --ink: #1a1512;
    --dots: #2a211b;
  }
  * { margin: 0; padding: 0; box-sizing: border-box; }
  html, body {
    width: 1200px;
    height: 900px;
    overflow: hidden;
    background: var(--backdrop);
  }
  .canvas {
    position: relative;
    width: 1200px;
    height: 900px;
    display: flex;
    align-items: center;
    justify-content: center;
  }
  .business-card {
    position: relative;
    width: 480px;
    height: 786px;
    background:
      radial-gradient(circle at 30% 20%, var(--kraft-light), transparent 60%),
      radial-gradient(circle at 75% 85%, var(--kraft-dark), transparent 55%),
      var(--kraft);
    box-shadow: 0 6px 18px rgba(60, 45, 30, 0.25);
  }
  .brand {
    position: absolute;
    top: 104px;
    left: 0;
    right: 0;
    display: flex;
    align-items: center;
    justify-content: center;
    gap: 14px;
  }
  .brand-dot {
    width: 30px;
    height: 30px;
    border-radius: 50%;
    background: var(--orchid);
  }
  .brand-name {
    font-family: "Questrial", sans-serif;
    font-size: 52px;
    color: var(--ink);
    letter-spacing: 1px;
  }
  .divider {
    position: absolute;
    left: 0;
    width: 100%;
    border-top: 3px dotted var(--dots);
  }
  .divider--top { top: 409px; }
  .divider--bottom { top: 532px; }
  .name-band {
    position: absolute;
    top: 416px;
    left: 0;
    width: 100%;
    height: 104px;
    background: var(--orchid);
    display: flex;
    flex-direction: column;
    align-items: center;
    justify-content: center;
    gap: 4px;
  }
  .person-name {
    font-family: "Lobster Two", cursive;
    font-style: italic;
    font-weight: 700;
    font-size: 34px;
    color: var(--ink);
    line-height: 1.1;
  }
  .person-role {
    font-family: "Old Standard TT", serif;
    font-weight: 700;
    font-size: 22px;
    color: var(--ink);
  }
  .contact {
    position: absolute;
    top: 604px;
    left: 0;
    width: 100%;
    height: 134px;
  }
  .contact-list {
    list-style: none;
    text-align: center;
    font-family: "Old Standard TT", serif;
    font-weight: 700;
    color: var(--ink);
    font-size: 20px;
    line-height: 34px;
  }
  .contact-list .company { font-size: 18px; }
  .brace {
    position: absolute;
    top: -6px;
    width: 36px;
    height: 132px;
  }
  .brace--left { left: 14px; }
  .brace--right { right: 14px; }
</style>
</head>
<body>
<main class="canvas">
  <article class="business-card">
    <header class="brand">
      <span class="brand-dot" aria-hidden="true"></span>
      <span class="brand-name">The Lumo Fenn</span>
    </header>

    <hr class="divider divider--top">
    <section class="name-band">
      <h1 class="person-name">Mirela Vance</h1>
      <p class="person-role">Owner</p>
    </section>
    <hr class="divider divider--bottom">

    <section class="contact">
      <svg class="brace brace--left" viewBox="0 0 36 132" aria-hidden="true">
        <path d="M30 4 C14 6 18 30 18 50 C18 60 14 64 4 66 C14 68 18 72 18 82 C18 102 14 126 30 128"
              fill="none" stroke="var(--orchid)" stroke-width="6" stroke-linecap="round"/>
      </svg>
      <ul class="contact-list">
        <li class="company">The Lumo Fenn Organic &amp; Natural Soaps</li>
        <li>(416) 555-0142</li>
        <li>Mirela@thelumofenn.ca</li>
        <li>www.thelumofenn.ca</li>
      </ul>
      <svg class="brace brace--right" viewBox="0 0 36 132" aria-hidden="true">
        <path d="M6 4 C22 6 18 30 18 50 C18 60 22 64 32 66 C22 68 18 72 18 82 C18 102 22 126 6 128"
              fill="none" stroke="var(--orchid)" stroke-width="6" stroke-linecap="round"/>
      </svg>
    </section>
  </article>
</main>
</body>
</html>
```